Custom Real Estate Postcard for Buying Communities

We are a real estate company that owns/operates mobile home parks and want to send out a postcard to owners of these communities letting them know who our company is and let them know we want to buy their community. We are looking to create a postcard that introduces our company to the owner and also lets them know we want to buy their community - we are targeting older mom & pop type communities so we would like the postcard to have a home-y feel that makes the owner feel like our company will treat them fairly during the acquisition process
I have attached a few images from our communities that might look good on a postcard - you don't need to use all of them, I just included multiple so there are different options. please feel free to edit/enhance the images if needed.
Our company is Bright Meadow Holdings (BMH) and the logo is attached.
Text to be included somewhere on postcard: "We pride ourselves on active hands-on management in order to provide our residents quality communities at an affordable price.
BMH is a proven owner/operator and has the ability to purchase without any financing contingencies.
We provide a quick and easy closing. We do not retrade
Target Market(s)
Owners of Mobile Home Parks that BMH (our company) would like to acquire - small mom & pop owners that want to see that we aren't the big firm trying to come in and take over but a local company that will still treat the residents well
Industry/Entity Type
Real Estate
Colors
Designer to choose colors to be used in the design.
Requirements
Must have
- The BMH logo, at least one picture of a mobile home park from the attached pictures. And some version/form of the provided text. Info/contact section with website (www.bmhparks.example), email (info@bmhparks.example) and phone (555.284.7160)
- Something sort of call to action like: "We Want to Buy Your Community", "Ready to Sell?", "Interested in Selling?" etc.
Nice to have
- BMH Logo Colors, in addition to any other colors if designer thinks there are complimentary colors

```html
<!DOCTYPE html>
<html lang="en">
<head>
<meta charset="utf-8">
<title>Bright Meadow Holdings Postcard</title>
<link href="https://fonts.googleapis.com/css2?family=Bebas+Neue&family=Open+Sans:wght@400;600&display=swap" rel="stylesheet">
<style>
  :root {
    --backdrop: #c3c3c3;
    --tan: #a47a3e;
    --rust: #8a3320;
    --panel: #efefef;
    --white: #ffffff;
    --ink: #3a3a3a;
    --rule: #555555;
  }
  * { margin: 0; padding: 0; box-sizing: border-box; }
  html, body { width: 1200px; height: 651px; overflow: hidden; }
  body {
    background: var(--backdrop);
    position: relative;
    font-family: "Open Sans", Arial, sans-serif;
  }
  .card {
    position: absolute;
    top: 137px;
    width: 528px;
    height: 339px;
    overflow: hidden;
    box-shadow: 0 3px 6px rgba(0,0,0,0.35);
  }
  .card-front { left: 53px; background: var(--tan); }
  .card-back { left: 613px; background: var(--white); }
  .card svg.shapes { position: absolute; inset: 0; }

  .front-intro {
    position: absolute; left: 28px; top: 38px; width: 190px;
    color: var(--white); font-size: 13.6px; font-weight: 600; line-height: 1.28;
  }
  .front-headline {
    position: absolute; left: 27px; top: 114px;
    color: var(--white); font-family: "Bebas Neue", Impact, sans-serif;
    font-size: 44px; font-weight: 400; line-height: 48px; letter-spacing: 1.5px;
  }
  .front-closing {
    position: absolute; left: 28px; top: 264px; width: 310px;
    color: var(--white); font-size: 13.4px; font-weight: 600; line-height: 1.28;
  }
  .brand-tab {
    position: absolute; left: 379px; top: 0; width: 110px; height: 58px;
    background: var(--white); border-radius: 0 0 12px 12px;
    display: flex; align-items: center; justify-content: center; gap: 6px;
    padding: 0 8px;
  }
  .brand-mark { width: 9px; height: 9px; background: var(--rust); flex: none; }
  .brand-name {
    color: var(--rust); font-size: 10px; font-weight: 600; line-height: 1.1;
    text-transform: uppercase;
  }

  .back-brand {
    position: absolute; left: 76px; top: 24px;
    display: flex; align-items: center; gap: 7px;
  }
  .back-brand .brand-mark { width: 12px; height: 12px; }
  .back-brand .brand-name { font-size: 10.5px; }
  .back-about {
    position: absolute; left: 40px; top: 75px; width: 180px;
    color: var(--ink); font-size: 7.6px; line-height: 1.3; text-align: center;
  }
  .back-about p + p { margin-top: 9px; }
  .back-contact {
    position: absolute; left: 0; top: 283px; width: 260px;
    color: var(--white); text-align: center; white-space: nowrap;
  }
  .contact-links { font-size: 9.6px; }
  .contact-links span { margin: 0 4px; }
  .contact-phone { font-size: 15px; font-weight: 600; margin-top: 1px; }
  .stamp-box {
    position: absolute; left: 420px; top: 37px; width: 67px; height: 67px;
    border: 1.5px solid var(--rule);
  }
  .address-line {
    position: absolute; left: 303px; width: 178px; height: 1.5px; background: var(--rule);
  }
</style>
</head>
<body>

<section class="card card-front">
  <svg class="shapes" width="528" height="339" viewBox="0 0 528 339">
    <defs>
      <linearGradient id="parkTones" x1="0" y1="0" x2="0" y2="1">
        <stop offset="0" stop-color="#bcd3e6"/>
        <stop offset="0.08" stop-color="#3f6b3a"/>
        <stop offset="0.45" stop-color="#6f9a4c"/>
        <stop offset="0.8" stop-color="#8a9478"/>
        <stop offset="1" stop-color="#5f8a3e"/>
      </linearGradient>
    </defs>
    <path role="img" aria-label="Aerial photograph of a manufactured home community surrounded by forest"
          d="M200,0 H528 V248 C480,282 430,302 395,300 C300,292 232,205 216,120 C209,80 205,40 200,0 Z"
          fill="url(#parkTones)"/>
    <path d="M209,0 C214,100 268,222 382,262 C432,280 490,262 528,238"
          fill="none" stroke="var(--rust)" stroke-width="10"/>
    <path d="M230,110 C262,210 330,252 400,258 C450,262 495,250 528,236"
          fill="none" stroke="var(--rust)" stroke-width="5"/>
  </svg>

  <div class="brand-tab">
    <span class="brand-mark"></span>
    <span class="brand-name">Bright<br>Meadow<br>Holdings</span>
  </div>

  <p class="front-intro">BMH is a proven owner/ operator and has the ability to purchase without any financing contingencies.</p>
  <h1 class="front-headline">We want to<br>buy your<br>community</h1>
  <p class="front-closing">We pride ourselves on active hands-on management in order to provide our residents quality communities at an affordable price.</p>
</section>

<section class="card card-back">
  <svg class="shapes" width="528" height="339" viewBox="0 0 528 339">
    <rect x="0" y="0" width="260" height="339" fill="var(--panel)"/>
    <path d="M0,150 C40,222 150,250 260,228 V339 H0 Z" fill="var(--tan)"/>
    <path d="M0,146 C40,218 150,246 260,224" fill="none" stroke="var(--white)" stroke-width="7"/>
    <path d="M0,150 C20,190 120,230 260,212 V226 C150,246 40,218 0,168 Z" fill="var(--rust)"/>
    <path d="M0,160 C30,200 130,222 260,200" fill="none" stroke="var(--white)" stroke-width="3"/>
    <path d="M0,165 C40,210 140,226 260,205" fill="none" stroke="var(--rust)" stroke-width="4"/>
  </svg>

  <div class="back-brand">
    <span class="brand-mark"></span>
    <span class="brand-name">Bright<br>Meadow<br>Holdings</span>
  </div>

  <div class="back-about">
    <p>Bright Meadow Holdings (BMH) is a real estate investment company focused on manufactured housing communities (MHCs) in the Mid-Atlantic, Midwest and Southeast United States.</p>
    <p>BMH is actively expanding and was listed as the 37th-largest MHC owner in the country by a leading industry publication in 2017. We pride ourselves on active, hands-on management in order to provide our residents quality communities at an affordable price.</p>
  </div>

  <div class="back-contact">
    <p class="contact-links">www.bmhparks.example<span>|</span>info@bmhparks.example</p>
    <p class="contact-phone">555.284.7160</p>
  </div>

  <div class="stamp-box"></div>
  <div class="address-line" style="top:207px"></div>
  <div class="address-line" style="top:243px"></div>
  <div class="address-line" style="top:279px"></div>
</section>

</body>
</html>
```